Move the hackers to Wordpress

Yep, we want to move https://www.brasslantern.com/ to Wordpress. It'll make it easier to update and add content. I'd like mostly the same look, but I'm not stuck with it.
Updates

DO NOT RESPOND OUTSIDE OF PIXEL BAZAAR OR CONTACT US DIRECTLY.

Industry/Entity Type

Computer Security

Coding

Coded - Design and coding required

Font styles to use
Sans Serif

Colors
ec1f27

Requirements
Must have
• What I do want is:
• 1. Similar look to the existing site
• 2. Needs to work on one of the Wordpress hosting sites. I do NOT want to run my own Wordpress server.
• 3. Keep the animation in the top panel.
• 4. Mobile support
• The rest can be changed as needed.
Nice to have
• I like the transitions when the "services" panel shows up. Not stuck on it, but it is a nice touch.

```html
<!DOCTYPE html>
<html lang="en">
<head>
<meta charset="utf-8">
<title>Brass Lantern – Information Security</title>
<link rel="stylesheet" href="https://fonts.googleapis.com/css2?family=Lato:wght@400;700;900&display=swap">
<style>
:root{
  --red:#ec1f27;
  --red-band:#d51f26;
  --red-deep:#bd171e;
  --ink:#222;
  --muted:#555;
  --light:#f4f4f4;
  --footer:#1b1b1b;
  --footer-field:#2b2b2b;
  --white:#fff;
}
*{box-sizing:border-box;margin:0;padding:0}
html,body{width:1200px;height:3666px;overflow:hidden}
body{font-family:"Lato",Arial,sans-serif;color:var(--ink);background:var(--white);position:relative}
section,header,footer{position:relative;width:1200px;overflow:hidden}
.abs{position:absolute}
.btn{position:absolute;display:flex;align-items:center;justify-content:center;background:var(--red);color:var(--white);font-size:14px;font-weight:700;border-radius:20px;height:38px;width:150px}
.btn.white{background:var(--white);color:var(--red)}

/* header */
.site-header{height:137px;background:var(--light)}
.brand{left:117px;top:44px;display:flex;align-items:center;gap:12px}
.brand-mark{width:40px;height:40px;background:var(--red)}
.brand-name{font-size:30px;font-weight:900;color:var(--red);letter-spacing:1px;line-height:1}
.brand-sub{font-size:10px;letter-spacing:3px;color:var(--ink);font-weight:700;margin-top:4px}
.nav{right:118px;top:62px;display:flex;gap:32px;font-size:15px;font-weight:700;color:var(--ink)}

/* hero */
.hero{height:633px;background:linear-gradient(120deg,#2a2c31 0%,#55585f 40%,#3a3c42 70%,#1d1e22 100%)}
.hero-title{top:290px;left:0;width:1200px;text-align:center;color:var(--white);font-size:32px;line-height:1.25}
.hero-title b{font-weight:700}
.hero .btn{top:388px;left:525px;width:148px}
.hero-arrow{top:296px;width:26px;height:26px}

/* what we do */
.what{height:550px;background:var(--light)}
.dots{top:20px;left:582px;display:flex;gap:6px}
.dots span{width:6px;height:6px;border-radius:50%;background:#555}
.dots span:first-child{background:var(--red)}
.section-title{left:0;width:1200px;text-align:center;font-size:32px;font-weight:400}
.what .section-title{top:54px}
.what-copy{top:139px;left:120px;width:455px;font-size:13px;line-height:1.4;color:#333}
.what-copy p+p{margin-top:18px}
.what .btn{top:361px;left:120px}
.devices{top:134px;left:590px;width:540px;height:340px;border-radius:6px;background:linear-gradient(160deg,#2a2a2e 0%,#4a1517 55%,#1f1f22 100%)}

/* services */
.services{height:532px;background:var(--red-band);color:var(--white)}
.services .section-title{top:48px;font-size:32px;color:var(--white)}
.svc-highlight{left:442px;top:115px;width:306px;height:168px;background:var(--red-deep)}
.service{width:290px}
.svc-head{display:flex;align-items:center;gap:12px;height:48px}
.svc-head svg{flex:none}
.svc-head h3{font-size:15px;font-weight:700;line-height:1.15}
.service p{font-size:12.5px;line-height:1.35;margin-top:12px;font-weight:700}
.read-more{font-size:12.5px;margin-top:4px;display:flex;align-items:center;gap:6px;font-weight:700}
.read-more i{width:12px;height:12px;border-radius:50%;background:currentColor;display:inline-block}

/* blogs */
.blogs{height:592px;background:var(--light)}
.blogs .section-title{top:70px;font-size:32px}
.blogs-sub{top:117px;left:0;width:1200px;text-align:center;font-size:13px;font-weight:700}
.post{top:154px;width:293px;height:340px}
.post-image{width:293px;height:115px;background:linear-gradient(135deg,#2e3640,#6d7d8c)}
.post-image.pink{background:linear-gradient(135deg,#3a2a30,#b3475c)}
.post-image.dark{background:linear-gradient(135deg,#0f1a2a,#3e5670)}
.post-date{position:absolute;top:0;left:0;width:34px;height:30px;background:var(--red);color:var(--white);font-size:10px;text-align:center;line-height:1.2;padding-top:3px;font-weight:700}
.post h3{font-size:12.5px;font-weight:900;margin-top:20px;text-transform:uppercase}
.post-meta{display:flex;align-items:center;font-size:12px;margin-top:6px;gap:6px;color:#333}
.post-meta .grow{flex:1}
.post p{font-size:13px;line-height:1.35;margin-top:8px;font-weight:700}
.post .read-more{color:var(--ink);font-weight:400;margin-top:6px}
.post .read-more i{background:none;border:1px solid #555}
.blogs .btn{top:526px;left:525px}

/* testimonials */
.testimonials{height:533px;background:var(--red-band);color:var(--white)}
.testimonials .section-title{top:40px;font-size:30px;font-weight:700;color:var(--white)}
.avatar{border-radius:50%;background:linear-gradient(180deg,#d98a8e,#b7484e)}
.avatar.main{left:508px;top:103px;width:186px;height:186px;border:6px solid var(--white);background:linear-gradient(180deg,#d7dde4,#5a6f87)}
.avatar.side-left{left:347px;top:125px;width:142px;height:142px}
.avatar.side-right{left:721px;top:125px;width:142px;height:142px}
.t-arrow{top:183px;width:26px;height:26px}
.t-name{top:295px;left:0;width:1200px;text-align:center;font-size:17px;font-weight:900}
.t-role{top:325px;left:0;width:1200px;text-align:center;font-size:13px;font-weight:700}
.t-quote{top:358px;left:410px;width:380px;text-align:center;font-size:13px;line-height:1.4;font-weight:700}
.t-mark{font-size:34px;font-weight:900;line-height:1}
.testimonials .btn{top:459px;left:525px}

/* newsletter */
.newsletter{height:323px;background:var(--light)}
.newsletter h2{top:110px;left:0;width:1200px;text-align:center;font-size:25px;font-weight:400}
.newsletter-sub{top:148px;left:0;width:1200px;text-align:center;font-size:13px}
.subscribe{top:205px;left:313px;width:574px;height:39px;display:flex;border-radius:20px;overflow:hidden}
.subscribe span{flex:1;background:#e4e4e4;color:#888;font-size:13px;display:flex;align-items:center;padding-left:22px}
.subscribe b{width:144px;background:var(--red);color:var(--white);font-size:14px;display:flex;align-items:center;justify-content:center;font-weight:900}

/* footer */
.site-footer{height:317px;background:var(--footer);color:var(--white)}
.site-footer .brand{left:117px;top:62px;gap:8px}
.site-footer .brand-mark{width:30px;height:30px}
.site-footer .brand-name{font-size:19px;letter-spacing:.5px}
.site-footer .brand-sub{color:var(--white);font-size:7px;letter-spacing:2px;margin-top:3px}
.footer-about{top:128px;left:117px;width:245px;font-size:13px;line-height:1.3;font-weight:700}
.footer-head{top:80px;font-size:13px;font-weight:900;padding-bottom:6px;border-bottom:2px solid var(--white);text-transform:uppercase}
.quick-links{top:116px;left:401px;font-size:13px;line-height:1.7;list-style:none}
.quick-links li::before{content:"›";margin-right:10px}
.contact-table{top:118px;left:543px;font-size:13px;border-collapse:collapse}
.contact-table td{padding:0 12px 14px 0;vertical-align:top}
.field{background:var(--footer-field);color:#aaa;font-size:11px;padding:6px 12px}
.site-footer .btn{height:28px;width:146px;font-size:12px}
.bottom-bar{height:49px;background:var(--light)}
.legal{top:17px;left:117px;font-size:13px}
.social{top:17px;right:118px;display:flex;gap:24px}
.social span{width:14px;height:14px;border-radius:50%;background:var(--ink)}
</style>
</head>
<body>

<header class="site-header">
  <div class="brand abs">
    <div class="brand-mark"></div>
    <div>
      <div class="brand-name">BRASS LANTERN</div>
      <div class="brand-sub">INFORMATION SECURITY</div>
    </div>
  </div>
  <nav class="nav abs"><span>Home</span><span>Services</span><span>Blog</span><span>Press</span><span>Contact</span></nav>
</header>

<section class="hero" role="img" aria-label="Hands typing on a laptop keyboard in a dim office">
  <svg class="hero-arrow abs" style="left:50px" viewBox="0 0 26 26"><circle cx="13" cy="13" r="13" fill="#fff"/><path d="M15 8l-5 5 5 5" stroke="#222" stroke-width="2.5" fill="none"/></svg>
  <svg class="hero-arrow abs" style="left:1124px" viewBox="0 0 26 26"><circle cx="13" cy="13" r="13" fill="#ec1f27"/><path d="M11 8l5 5-5 5" stroke="#fff" stroke-width="2.5" fill="none"/></svg>
  <h1 class="hero-title abs"><b>Offensive Services</b> From<br>Offensive minds</h1>
  <div class="btn">Read More</div>
</section>

<section class="what">
  <div class="dots abs"><span></span><span></span><span></span><span></span></div>
  <h2 class="section-title abs">What we do</h2>
  <div class="what-copy abs">
    <p>We are an information security company focusing on real world threats. Brass Lantern is an information security consulting company that concentrates on the latest threats to organizations today. We perform in-depth analysis, determine organization/business risk, and find the vulnerabilities before the bad guys do.</p>
    <p>Our team includes internationally renowned experts who have been featured in international news outlets and conferences, including The Morning Ledger, The Capital Courier, a Pacific News Network Documentary</p>
  </div>
  <div class="btn">Read More</div>
  <div class="devices abs" role="img" aria-label="Desktop, laptop, tablet and phone showing the Brass Lantern site"></div>
</section>

<section class="services">
  <h2 class="section-title abs">Services</h2>
  <div class="svc-highlight abs"></div>

  <div class="service abs" style="left:117px;top:141px">
    <div class="svc-head"><svg width="48" height="48" viewBox="0 0 48 48" fill="none" stroke="#fff" stroke-width="3"><rect x="6" y="4" width="28" height="38" rx="3"/><circle cx="28" cy="30" r="9"/><path d="M24 30l3 3 6-6"/></svg><h3>Internal Pivot Assessment<br>&amp; Post Exploitation</h3></div>
    <p>Lorem Ipsum is simply dummy text of the of the printing and typesetting industry.</p>
    <div class="read-more">Read More.. <i></i></div>
  </div>
  <div class="service abs" style="left:472px;top:141px">
    <div class="svc-head"><svg width="48" height="48" viewBox="0 0 48 48" fill="none" stroke="#fff" stroke-width="3"><circle cx="22" cy="26" r="17"/><circle cx="22" cy="26" r="9"/><circle cx="22" cy="26" r="2" fill="#fff"/><path d="M22 26L42 6M36 6h6v6"/></svg><h3>Red team Adversary<br>Simulation</h3></div>
    <p>Lorem Ipsum is simply dummy text of the of the printing and typesetting industry.</p>
    <div class="read-more">Read More.. <i></i></div>
  </div>
  <div class="service abs" style="left:816px;top:141px">
    <div class="svc-head"><svg width="48" height="48" viewBox="0 0 48 48" fill="none" stroke="#fff" stroke-width="3"><rect x="17" y="4" width="14" height="11"/><rect x="3" y="33" width="12" height="11"/><rect x="18" y="33" width="12" height="11"/><rect x="33" y="33" width="12" height="11"/><path d="M24 15v18M9 33v-9h30v9"/></svg><h3>Penetration testing &amp;<br>Vulnerability Assessments</h3></div>
    <p>Lorem Ipsum is simply dummy text of the of the printing and typesetting industry.</p>
    <div class="read-more">Read More.. <i></i></div>
  </div>

  <div class="service abs" style="left:117px;top:330px">
    <div class="svc-head"><svg width="48" height="48" viewBox="0 0 48 48" fill="none" stroke="#fff" stroke-width="3"><path d="M8 40L30 18M30 18a8 8 0 1 0 0-2M40 40L10 10M6 6l8 2-6 6z"/></svg><h3>Advanced Product,<br>Hardware &amp; Rf Testing</h3></div>
    <p>Lorem Ipsum is simply dummy text of the of the printing and typesetting industry.</p>
    <div class="read-more">Read More.. <i></i></div>
  </div>
  <div class="service abs" style="left:472px;top:330px">
    <div class="svc-head"><svg width="48" height="48" viewBox="0 0 48 48" fill="none" stroke="#fff" stroke-width="3"><rect x="6" y="8" width="36" height="26" rx="2"/><path d="M2 38h44M19 16l-5 5 5 5M29 16l5 5-5 5M26 15l-4 12"/></svg><h3>Web Application<br>Penetration Testing</h3></div>
    <p>Lorem Ipsum is simply dummy text of the of the printing and typesetting industry.</p>
    <div class="read-more">Read More.. <i></i></div>
  </div>
  <div class="service abs" style="left:816px;top:330px">
    <div class="svc-head"><svg width="48" height="48" viewBox="0 0 48 48" fill="none" stroke="#fff" stroke-width="3"><rect x="6" y="4" width="20" height="40" rx="3"/><path d="M14 38h4"/><circle cx="34" cy="18" r="6"/><path d="M34 8v4M34 24v4M24 18h4M40 18h4"/></svg><h3>Mobile Application<br>Assessment</h3></div>
    <p>Lorem Ipsum is simply dummy text of the of the printing and typesetting industry.</p>
    <div class="read-more">Read More.. <i></i></div>
  </div>
</section>

<section class="blogs">
  <h2 class="section-title abs">Our Blogs</h2>
  <div class="blogs-sub abs">Lorem Ipsum is simply dummy text.</div>

  <article class="post abs" style="left:122px">
    <div class="post-image" role="img" aria-label="Padlock and chain wrapped around a keyboard"></div>
    <div class="post-date">01<br>Jun</div>
    <h3>5 Computer Security Facts</h3>
    <div class="post-meta"><svg width="11" height="11" viewBox="0 0 11 11"><rect x=".5" y="1.5" width="10" height="9" fill="none" stroke="#333"/><path d="M.5 4h10" stroke="#333"/></svg><span class="grow">June 20, 2018</span><svg width="12" height="11" viewBox="0 0 12 11"><path d="M1 1h10v7H5l-3 2V8H1z" fill="none" stroke="#333"/></svg>20<span style="width:12px"></span><svg width="12" height="11" viewBox="0 0 12 11"><path d="M6 10L1 5a2.5 2.5 0 0 1 5-3 2.5 2.5 0 0 1 5 3z" fill="none" stroke="#333"/></svg>12</div>
    <p>Lorem Ipsum is simply dummy text of the printing and typesetting industry.</p>
    <div class="read-more">Read More.. <i></i></div>
  </article>

  <article class="post abs" style="left:455px">
    <div class="post-image pink" role="img" aria-label="Monitor showing a cyber training range screen"></div>
    <div class="post-date">01<br>Jun</div>
    <h3>TV Post Title</h3>
    <div class="post-meta"><svg width="11" height="11" viewBox="0 0 11 11"><rect x=".5" y="1.5" width="10" height="9" fill="none" stroke="#333"/><path d="M.5 4h10" stroke="#333"/></svg><span class="grow">June 20, 2018</span><svg width="12" height="11" viewBox="0 0 12 11"><path d="M1 1h10v7H5l-3 2V8H1z" fill="none" stroke="#333"/></svg>20<span style="width:12px"></span><svg width="12" height="11" viewBox="0 0 12 11"><path d="M6 10L1 5a2.5 2.5 0 0 1 5-3 2.5 2.5 0 0 1 5 3z" fill="none" stroke="#333"/></svg>12</div>
    <p>Lorem Ipsum is simply dummy text off printing and typesetting industry.</p>
    <div class="read-more">Read More.. <i></i></div>
  </article>

  <article class="post abs" style="left:787px">
    <div class="post-image dark" role="img" aria-label="Hooded figure at a laptop in front of binary code"></div>
    <div class="post-date">01<br>Oct</div>
    <h3>TV Post Title</h3>
    <div class="post-meta"><svg width="11" height="11" viewBox="0 0 11 11"><rect x=".5" y="1.5" width="10" height="9" fill="none" stroke="#333"/><path d="M.5 4h10" stroke="#333"/></svg><span class="grow">Febuary 22, 2018</span><svg width="12" height="11" viewBox="0 0 12 11"><path d="M1 1h10v7H5l-3 2V8H1z" fill="none" stroke="#333"/></svg>20<span style="width:12px"></span><svg width="12" height="11" viewBox="0 0 12 11"><path d="M6 10L1 5a2.5 2.5 0 0 1 5-3 2.5 2.5 0 0 1 5 3z" fill="none" stroke="#333"/></svg>12</div>
    <p>Lorem Ipsum is simply dummy text off printing and typesetting industry.</p>
    <div class="read-more">Read More.. <i></i></div>
  </article>

  <div class="btn">Read More</div>
</section>

<section class="testimonials">
  <h2 class="section-title abs">Testimonials</h2>
  <svg class="t-arrow abs" style="left:283px" viewBox="0 0 26 26"><path d="M16 7l-6 6 6 6" stroke="#fff" stroke-width="3" fill="none"/></svg>
  <svg class="t-arrow abs" style="left:891px" viewBox="0 0 26 26"><path d="M10 7l6 6-6 6" stroke="#fff" stroke-width="3" fill="none"/></svg>
  <div class="avatar side-left abs" role="img" aria-label="Client portrait"></div>
  <div class="avatar side-right abs" role="img" aria-label="Client portrait"></div>
  <div class="avatar main abs" role="img" aria-label="Portrait of Martin Hale"></div>
  <div class="t-name abs">MARTIN HALE</div>
  <div class="t-role abs">Creative Director</div>
  <div class="t-quote abs"><span class="t-mark abs" style="left:-8px;top:-20px">“</span>Lorem Ipsum is simply dummy text of the printing and typesettingindustry. Lorem Ipsum has been the industry's standard dummy text ever since the 1500s,<span class="t-mark abs" style="right:-8px;bottom:-18px">”</span></div>
  <div class="btn white">Read More</div>
</section>

<section class="newsletter">
  <h2 class="abs">Subscribe To Our Newsletter</h2>
  <div class="newsletter-sub abs">To Receive The latest News And Update</div>
  <div class="subscribe abs"><span>Your E-Mail</span><b>SUBMIT</b></div>
</section>

<footer class="site-footer">
  <div class="brand abs">
    <div class="brand-mark"></div>
    <div>
      <div class="brand-name">BRASS LANTERN</div>
      <div class="brand-sub">INFORMATION SECURITY</div>
    </div>
  </div>
  <p class="footer-about abs">Lorem Ipsum is simply dummy in text of the printing and typesetting industry. Lorem Ipsum<br>Read More.. ⊕</p>

  <div class="footer-head abs" style="left:401px">Quick Link</div>
  <ul class="quick-links abs"><li>Home</li><li>Services</li><li>Blog</li><li>Press</li><li>Contact</li></ul>

  <div class="footer-head abs" style="left:543px">Contact Us</div>
  <table class="contact-table abs">
    <tr><td>Address :</td><td>48 Harbor Lane,<br>USA</td></tr>
    <tr><td>Phone</td><td>:&nbsp; +1.555.014.2290</td></tr>
    <tr><td>E-mail</td><td>:&nbsp; contact@brasslantern.com</td></tr>
  </table>

  <div class="footer-head abs" style="left:807px">Quick Contact</div>
  <div class="field abs" style="left:807px;top:131px;width:131px;height:28px">Name</div>
  <div class="field abs" style="left:948px;top:131px;width:132px;height:28px">Phone</div>
  <div class="field abs" style="left:807px;top:166px;width:273px;height:62px">Message</div>
  <div class="btn" style="left:807px;top:256px">SEND</div>
</footer>

<div class="bottom-bar" style="position:relative">
  <div class="legal abs">Privacy policy - Legal Mentions - Terms and Conditions</div>
  <div class="social abs"><span></span><span></span><span></span><span></span><span></span></div>
</div>

</body>
</html>
```